Old boys day 2025

HARTLEY FALCONS V BROOKVALE BULLS SUNDAY 10TH AUGUST
THIS IS A FREE EVENT FOR NEST MEMBERS
THE NEST WOULD LIKE TO WELCOME ALL PAST PLAYERS,
COACHES, COMMITTEE, SPONSORS & SUPPORTERS TO OUR
ANNUAL FALCON DAY OF CELEBRATION.
JOIN US IN THE PADDOCK FOR A GREAT DAY OF LEAGUE ACTION
WATCHING OUR CURRENT CROP OF FALCONS. YOU CAN PURCHASE A TICKET AND OR JOIN THE NEST @ WWW.HARTLEYNEST.COM.AU
IF YOU JOIN THE NEST PRIOR TO THE EVENT OLD BOYS DAY IS FREE OF CHARGE, YOU STILL NEED TO
PURCHASE/REGISTER A TICKET ON THE EVENTS PAGE SO WE KNOW YOU ARE ATTENDING.
WE WILL BE HONOURING 6 PREMIERSHIP WINNING TEAMS THIS YEAR: 1935 1ST GRADE (90 YEARS), 1980 RESERVE GRADE (45 YEARS), 1985 1ST GRADE (40 YEARS), 1985 U18'S (40 YEARS), 2005 1ST GRADE (20 YEARS) & 2015 1ST GRADE (10 YEARS)
IN THE 1ST GRADE GAME THE PLAYERS WILL BE WEARING REPLICA 1985 JERSEYS (attached) WITH THE 85 PLAYERS NAMES ON THE BACK, THE NEST WILL BE HOSTING A POST GAME FUNCTION AT THE WREN GATE INN WHERE THESE JERSEYS WILL BE AUCTIONED OFF TO RAISE MONEY.
PURCHASE YOUR TICKET AT WWW.HARTLEYNEST.COM.AU/EVENTS

Target Market(s)

ex players

Requirements
Must have
• I NEED A A4 FLYER DESIGN & A DESIGN THAT WILL SUIT SOCIAL MEDIA

```html
<!DOCTYPE html>
<html lang="en">
<head>
<meta charset="utf-8">
<title>The Nest Old Boys Day 2025</title>
<link rel="stylesheet" href="https://fonts.googleapis.com/css2?family=Bebas+Neue&family=Roboto+Condensed:wght@400;500&display=swap">
<style>
  :root {
    --crimson: #a5193c;
    --gold: #b98a58;
    --gold-light: #e6cfae;
    --gold-dark: #8c6238;
    --charcoal: #2b2b2b;
    --charcoal-soft: #4a4a4a;
    --ink: #1c1c1c;
    --paper: #ffffff;
    --mist: #e9e9e9;
  }
  * { margin: 0; padding: 0; box-sizing: border-box; }
  html, body { width: 848px; height: 1200px; overflow: hidden; background: var(--paper); }
  .flyer { position: relative; width: 848px; height: 1200px; overflow: hidden; font-family: "Roboto Condensed", sans-serif; color: var(--ink); }
  .abs { position: absolute; }
  .display { font-family: "Bebas Neue", sans-serif; letter-spacing: 0.5px; }

  /* hero */
  .hero-photo { left: 0; top: 0; width: 848px; height: 170px; background: linear-gradient(180deg, #3c3c3c 0%, #5a5a5a 55%, #4a4a4a 100%); }
  .hero-title { left: 0; width: 848px; text-align: center; line-height: 1; }
  .hero-title.small { top: 40px; font-size: 56px; background: linear-gradient(90deg, var(--gold-dark), var(--gold-light), var(--gold)); -webkit-background-clip: text; background-clip: text; color: transparent; }
  .hero-title.big { top: 84px; font-size: 66px; color: var(--paper); }

  /* matchup */
  .matchup { left: 0; top: 160px; }
  .team { color: var(--paper); font-size: 31px; line-height: 33px; font-weight: 500; }
  .team.home { right: 503px; top: 186px; text-align: right; }
  .team.away { left: 506px; top: 186px; }
  .versus { left: 368px; top: 170px; width: 112px; text-align: center; font-size: 88px; line-height: 1; color: var(--paper); }
  .match-date { left: 0; top: 268px; width: 848px; text-align: center; color: var(--paper); font-size: 46px; line-height: 1; }
  .club-mark { top: 208px; width: 150px; text-align: center; font-size: 30px; line-height: 30px; }
  .club-mark.home { left: 12px; color: var(--ink); }
  .club-mark.away { left: 690px; color: var(--crimson); }

  /* info panel */
  .info-panel { left: 0; top: 324px; width: 848px; height: 398px; background: radial-gradient(ellipse at 50% 40%, var(--charcoal-soft) 0%, var(--charcoal) 70%); }
  .free-pill { left: 96px; top: 353px; width: 655px; height: 51px; border: 2px solid var(--gold); border-radius: 26px; color: var(--paper); font-size: 31px; line-height: 47px; text-align: center; }
  .welcome, .join { left: 0; width: 848px; text-align: center; color: var(--paper); font-size: 22.5px; line-height: 24px; }
  .welcome { top: 430px; }
  .celebration { left: 0; top: 492px; width: 848px; text-align: center; font-size: 55px; line-height: 1; background: linear-gradient(90deg, var(--gold-dark), var(--gold-light) 50%, var(--gold)); -webkit-background-clip: text; background-clip: text; color: transparent; }
  .join { top: 556px; }
  .site-link { left: 0; top: 647px; width: 848px; text-align: center; font-size: 38px; line-height: 55px; color: var(--charcoal); }

  /* notice */
  .notice { left: 0; top: 722px; width: 848px; height: 83px; background: linear-gradient(90deg, var(--gold) 0%, var(--gold-light) 50%, var(--gold) 100%); text-align: center; font-size: 21px; line-height: 22px; padding-top: 10px; color: var(--ink); }

  /* honours */
  .honours { left: 0; top: 805px; width: 848px; height: 331px; background: linear-gradient(90deg, var(--paper) 0%, var(--mist) 100%); }
  .honours-strip { left: 0; top: 1040px; width: 848px; height: 96px; background: linear-gradient(90deg, var(--gold-light) 0%, var(--gold) 70%, var(--gold-dark) 100%); }
  .nest-mark { left: 30px; top: 900px; width: 165px; font-size: 44px; line-height: 44px; color: var(--ink); display: flex; align-items: center; gap: 8px; }
  .nest-mark .dot { width: 14px; height: 14px; background: var(--ink); flex: none; }
  .honour-banner-text { left: 203px; top: 845px; color: var(--paper); font-size: 18.5px; line-height: 19px; font-weight: 500; }
  .honour-list { left: 203px; top: 898px; list-style: none; font-size: 18px; line-height: 18px; color: var(--ink); }
  .jersey-art { left: 520px; top: 860px; width: 316px; height: 272px; border-radius: 40px 40px 6px 6px; background: linear-gradient(160deg, #f7f7f7 0%, #dcdcdc 100%); box-shadow: 0 0 0 3px var(--ink) inset; }
  .jersey-note { right: 285px; top: 1049px; text-align: right; font-size: 16px; line-height: 16.5px; color: var(--ink); }

  .footer { left: 0; top: 1136px; width: 848px; height: 64px; background: var(--crimson); color: var(--paper); text-align: center; font-size: 40px; line-height: 66px; }
</style>
</head>
<body>
<main class="flyer">
  <div class="abs hero-photo" role="img" aria-label="Team photo of past premiership players in black and white jerseys"></div>
  <h1 class="abs hero-title small display">THE NEST</h1>
  <h2 class="abs hero-title big display">OLD BOYS DAY 2025</h2>

  <svg class="abs matchup" width="848" height="164" viewBox="0 160 848 164" aria-hidden="true">
    <defs>
      <linearGradient id="goldBar" x1="0" x2="1">
        <stop offset="0" stop-color="#8c6238"/>
        <stop offset="0.5" stop-color="#d9b78d"/>
        <stop offset="1" stop-color="#8c6238"/>
      </linearGradient>
    </defs>
    <polygon points="0,160 142,160 213,311 0,311" fill="#ffffff"/>
    <polygon points="707,160 848,160 848,311 636,311" fill="#ffffff"/>
    <polygon points="142,173 707,173 676,262 173,262" fill="url(#goldBar)"/>
    <polygon points="173,262 676,262 636,311 213,311" fill="#a5193c"/>
    <rect x="0" y="311" width="848" height="13" fill="#a5193c"/>
  </svg>
  <div class="abs club-mark home display">HARTLEY FALCONS</div>
  <div class="abs club-mark away display">BROOKVALE BULLS</div>
  <div class="abs team home">HARTLEY<br>FALCONS</div>
  <div class="abs versus display">VS</div>
  <div class="abs team away">BROOKVALE<br>BULLS</div>
  <div class="abs match-date display">SUNDAY 10TH AUGUST</div>

  <section class="abs info-panel"></section>
  <div class="abs free-pill">THIS IS A FREE EVENT FOR NEST MEMBERS</div>
  <p class="abs welcome">THE NEST WOULD LIKE TO WELCOME ALL PAST PLAYERS,<br>COACHES, COMMITTEE, SPONSORS &amp; SUPPORTERS TO OUR</p>
  <p class="abs celebration display">ANNUAL FALCON DAY OF CELEBRATION</p>
  <p class="abs join">JOIN US IN THE PADDOCK FOR A GREAT DAY OF LEAGUE ACTION<br>WATCHING OUR CURRENT CROP OF FALCONS.<br>YOU CAN PURCHASE A TICKET AND OR JOIN THE NEST</p>
  <svg class="abs" style="left:0;top:647px" width="848" height="55" aria-hidden="true">
    <defs>
      <linearGradient id="linkBar" x1="0" x2="1">
        <stop offset="0" stop-color="#a77a4b"/>
        <stop offset="0.5" stop-color="#ecd9bd"/>
        <stop offset="1" stop-color="#a77a4b"/>
      </linearGradient>
    </defs>
    <polygon points="212,0 658,0 634,55 188,55" fill="url(#linkBar)"/>
  </svg>
  <div class="abs site-link display">WWW.HARTLEYNEST.COM.AU</div>

  <p class="abs notice">IF YOU JOIN THE NEST PRIOR TO THE EVENT OLD BOYS DAY IS<br>FREE OF CHARGE, YOU STILL NEED TO PURCHASE/REGISTER A TICKET<br>ON THE EVENTS PAGE SO WE KNOW YOU ARE ATTENDING</p>

  <section class="abs honours"></section>
  <div class="abs honours-strip"></div>
  <div class="abs nest-mark display"><span class="dot"></span>THE NEST</div>
  <svg class="abs" style="left:187px;top:836px" width="370" height="53" aria-hidden="true">
    <polygon points="0,0 370,0 348,53 0,53" fill="#a5193c"/>
  </svg>
  <p class="abs honour-banner-text">WE WILL BE HONOURING 6 PREMIERSHIP<br>WINNING TEAMS THIS YEAR</p>
  <ul class="abs honour-list">
    <li>1935 1ST GRADE (90 YEARS)</li>
    <li>1980 RESERVE GRADE (45 YEARS)</li>
    <li>1985 1ST GRADE (40 YEARS)</li>
    <li>1985 U18'S (40 YEARS)</li>
    <li>2005 1ST GRADE (20 YEARS)</li>
    <li>2015 1ST GRADE (10 YEARS)</li>
  </ul>
  <div class="abs jersey-art" role="img" aria-label="Replica 1985 white jersey with black chevron and sponsor name"></div>
  <p class="abs jersey-note">IN THE 1ST GRADE GAME THE PLAYERS WILL BE WEARING<br>REPLICA 1985 JERSEYS WITH THE 85 PLAYERS NAMES ON THE BACK.<br>THE NEST WILL BE HOSTING A POST GAME FUNCTION AT THE WREN GATE INN<br>WHERE THESE JERSEYS WILL BE AUCTIONED OFF TO RAISE MONEY.</p>

  <footer class="abs footer display">PURCHASE YOUR TICKET AT WWW.HARTLEYNEST.COM.AU/EVENTS</footer>
</main>
</body>
</html>
```